Communications Contractor Business Card Design

I would like a new business card for a new Communications company in Australia. Subcontracting and specialising in cabling, data, phone, antennas, pay tv ,modems, audio visual fibre optics etc. I am open to colour and design concepts but would like a modern clean look that stands out.

Industry/Entity Type

Tv

Contact Information for Business Card

kestrel communications pty ltd, Doug Pemberton, PO BOX 657 Marlow Flats QLD 4873 kestrel4me@maildrop-example.com Australia. ph 0437196084. Director/Technician. services- Cabling,data,phone,antennas,audio visual,home theatre, fibre optics.

```html
<!DOCTYPE html>
<html lang="en">
<head>
<meta charset="utf-8">
<title>Kestrel Communications – Business Card</title>
<link rel="stylesheet" href="https://fonts.googleapis.com/css2?family=Arimo:wght@400;700&display=swap">
<style>
  :root {
    --page-bg: #ececec;
    --card-white: #ffffff;
    --ink: #111111;
    --brand-dark: #1c1c1c;
    --name-blue: #3a4fa3;
    --title-red: #d42a2a;
    --services-red: #9c1c1c;
    --swirl-pale: #dfe9f6;
    --swirl-mid: #6fa3dc;
    --swirl-deep: #1f64b8;
    --swirl-navy: #0c2a5e;
  }
  * { box-sizing: border-box; margin: 0; padding: 0; }
  html, body {
    width: 1200px; height: 1200px; overflow: hidden;
    background: var(--page-bg);
    font-family: "Arimo", Arial, sans-serif;
  }
  .card {
    position: absolute; left: 139px; width: 917px; height: 564px;
    background: var(--card-white);
    overflow: hidden;
    box-shadow: 0 6px 18px rgba(0,0,0,0.18);
  }
  .card--front { top: 22px; }
  .card--back { top: 614px; }

  .card__artwork {
    position: absolute; inset: 0;
  }
  .card--front .card__artwork {
    background:
      radial-gradient(ellipse 40% 30% at 98% 10%, var(--swirl-navy) 0%, transparent 70%),
      radial-gradient(ellipse 35% 70% at 95% 45%, var(--swirl-deep) 0%, transparent 75%),
      radial-gradient(ellipse 45% 90% at 78% 55%, var(--swirl-mid) 0%, transparent 70%),
      linear-gradient(90deg, var(--card-white) 38%, var(--swirl-pale) 62%, var(--swirl-mid) 100%);
    opacity: 0.95;
  }
  .card--back .card__artwork {
    background:
      radial-gradient(ellipse 30% 18% at 96% 12%, rgba(31,80,150,0.75) 0%, transparent 75%),
      radial-gradient(ellipse 40% 80% at 85% 50%, rgba(111,163,220,0.35) 0%, transparent 75%),
      linear-gradient(90deg, var(--card-white) 45%, #eef3fa 75%, #dbe6f4 100%);
  }

  .brand {
    position: absolute;
    color: var(--brand-dark);
    font-weight: 700;
    line-height: 1;
  }
  .brand__name { display: block; font-size: 80px; letter-spacing: 1px; }
  .brand__tagline { display: block; font-size: 27px; letter-spacing: 1.5px; margin-top: 8px; }
  .card--front .brand { left: 47px; top: 54px; }
  .card--back .brand { left: 0; right: 0; top: 232px; text-align: center; }

  .contact { position: absolute; left: 42px; top: 256px; }
  .contact__name { font-size: 30px; color: var(--name-blue); line-height: 1; }
  .contact__role { font-size: 21px; color: var(--title-red); margin-top: 10px; }
  .contact__line { font-size: 21px; color: var(--ink); margin-top: 18px; }
  .contact__line + .contact__line { margin-top: 13px; }

  .services { position: absolute; left: 42px; top: 460px; }
  .services__heading { font-size: 25px; color: var(--services-red); }
  .services__list { font-size: 22px; color: var(--ink); margin-top: 12px; white-space: nowrap; }
</style>
</head>
<body>
  <section class="card card--front">
    <div class="card__artwork" role="img" aria-label="Abstract flowing blue light streaks sweeping across the right side"></div>
    <div class="brand">
      <span class="brand__name">KESTREL</span>
      <span class="brand__tagline">COMMUNICATIONS PTY LTD</span>
    </div>
    <div class="contact">
      <p class="contact__name">Doug Pemberton</p>
      <p class="contact__role">Director/Technician.</p>
      <p class="contact__line">PO BOX 657 Marlow Flats QLD 4873 Australia.</p>
      <p class="contact__line">Phone : 0437196084.</p>
    </div>
    <div class="services">
      <p class="services__heading">Services</p>
      <p class="services__list">Cabling | data | phone | antennas | audio visual | home theatre | fibre optics.</p>
    </div>
  </section>

  <section class="card card--back">
    <div class="card__artwork" role="img" aria-label="Soft faded blue light streaks on a white background"></div>
    <div class="brand">
      <span class="brand__name">KESTREL</span>
      <span class="brand__tagline">COMMUNICATIONS PTY LTD</span>
    </div>
  </section>
</body>
</html>
```